Poster design needed for Pregnant class 25.11.2018*

We need a poster design with the instruction details:
- Size: A4- Content:
1. Logo
2. Title of poster: Pregnant class - Eating healthy while pregnant
3. Promote when join in out class: 30% off delivery package
4. Singapore - 25.11.2018
5. Detail of contact: please visit https://www.corbinridge.com.sg/And get information for this poster.

Target Market(s)

Pregnant

Industry/Entity Type

Medical And Science

Font styles to use
Sans Serif

Colors
85cae6
33a6d7

Requirements
Must have
• Picture mom and baby or pregnant

```html
<!DOCTYPE html>
<html lang="en">
<head>
<meta charset="utf-8">
<title>Pregnant Class – Corbin Ridge</title>
<link href="https://fonts.googleapis.com/css2?family=Great+Vibes&family=Oswald:wght@500&family=Open+Sans:wght@400;600&display=swap" rel="stylesheet">
<style>
  :root {
    --stage: #8a8a8a;
    --paper: #ebf2fc;
    --gold: #b3aa82;
    --blue: #33a6d7;
    --ink: #1f1f1f;
    --rule: #8c8c8c;
    --white: #ffffff;
  }
  html, body { margin: 0; padding: 0; overflow: hidden; }
  body { width: 1200px; height: 1200px; background: var(--stage); position: relative; font-family: "Open Sans", sans-serif; }
  .poster { position: absolute; left: 266px; top: 78px; width: 668px; height: 932px; background: var(--paper); overflow: hidden; }
  .brand-band { position: absolute; left: 0; top: 0; }
  .brand { position: absolute; left: 14px; top: 26px; display: flex; align-items: center; gap: 10px; }
  .brand-dot { width: 26px; height: 26px; border-radius: 50%; background: var(--white); }
  .brand-name { color: var(--white); font-size: 19px; font-weight: 400; }
  .tagline { position: absolute; left: 278px; top: 63px; font-size: 10px; font-weight: 600; letter-spacing: 2.5px; color: var(--gold); }
  .photo { position: absolute; left: 0; top: 180px; width: 360px; height: 752px;
    background: radial-gradient(ellipse at 50% 18%, #e9b98a 0%, #d9c8bb 22%, transparent 45%),
                linear-gradient(180deg, #eef2f8 0%, #f4eeea 40%, #f6f3f2 100%); }
  .title { position: absolute; left: 352px; width: 300px; text-align: center; font-family: "Great Vibes", cursive; color: var(--blue); font-size: 92px; line-height: 1; margin: 0; font-weight: 400; }
  .title-1 { top: 98px; }
  .title-2 { top: 184px; }
  .rule { position: absolute; height: 1px; background: var(--rule); }
  .subtitle { position: absolute; left: 366px; top: 306px; width: 280px; text-align: center; font-family: "Great Vibes", cursive; font-size: 44px; line-height: 46px; color: var(--ink); margin: 0; font-weight: 400; }
  .promo-lead { position: absolute; left: 364px; top: 462px; width: 280px; text-align: center; font-size: 17.5px; color: var(--ink); }
  .offer { position: absolute; left: 366px; top: 498px; width: 288px; height: 112px; background: var(--gold); outline: 1px dashed rgba(255,255,255,.7); outline-offset: -2px; color: var(--white); text-align: center; }
  .offer-amount { font-family: "Oswald", sans-serif; font-weight: 500; font-size: 62px; line-height: 1; margin-top: 8px; }
  .offer-item { font-size: 23px; line-height: 1; margin-top: 8px; }
  .event { position: absolute; left: 364px; top: 626px; width: 287px; height: 39px; border: 1px solid #444; box-sizing: border-box; font-size: 25px; font-weight: 600; color: var(--ink); text-align: center; line-height: 37px; }
  .contact { position: absolute; right: 30px; display: flex; align-items: center; gap: 4px; color: var(--ink); }
  .contact-icon { width: 18px; height: 18px; border-radius: 50%; background: var(--gold); display: flex; align-items: center; justify-content: center; }
  .contact-phone { top: 746px; font-size: 25px; font-weight: 600; }
  .contact-phone .contact-icon { width: 24px; height: 24px; }
  .contact-mail { top: 784px; font-size: 16px; font-weight: 600; }
  .contact-web { top: 814px; font-size: 16px; font-weight: 600; }
  .footer-band { position: absolute; left: 0; bottom: 0; width: 668px; height: 50px; background: var(--gold); }
</style>
</head>
<body>
  <main class="poster">
    <svg class="brand-band" width="310" height="76" viewBox="0 0 310 76" aria-hidden="true">
      <polygon points="0,0 308,0 252,76 0,76" fill="var(--gold)"/>
    </svg>
    <div class="brand"><span class="brand-dot"></span><span class="brand-name">Corbin Ridge</span></div>
    <div class="tagline">CARE FOR LIFE.</div>

    <div class="footer-band"></div>
    <div class="photo" role="img" aria-label="Photograph of a pregnant woman in a white dress holding her belly in soft sunset light"></div>

    <h1 class="title title-1">Pregnant</h1>
    <h1 class="title title-2">class</h1>
    <div class="rule" style="left:366px;top:290px;width:271px"></div>
    <h2 class="subtitle">Eating healthy while pregnant</h2>
    <div class="rule" style="left:374px;top:422px;width:258px"></div>

    <div class="promo-lead">Promote when join in out class</div>
    <div class="offer">
      <div class="offer-amount">30% Off</div>
      <div class="offer-item">Delivery package</div>
    </div>
    <div class="event">Singapore -25.11.2018</div>

    <div class="rule" style="left:456px;top:732px;width:180px"></div>
    <div class="contact contact-phone">
      <span class="contact-icon"><svg width="14" height="14" viewBox="0 0 24 24"><path d="M6.6 10.8a15 15 0 0 0 6.6 6.6l2.2-2.2c.3-.3.7-.4 1-.2 1.1.4 2.3.6 3.6.6.6 0 1 .4 1 1V20c0 .6-.4 1-1 1A17 17 0 0 1 3 4c0-.6.4-1 1-1h3.5c.6 0 1 .4 1 1 0 1.3.2 2.5.6 3.6.1.3 0 .7-.2 1z" fill="#fff"/></svg></span>
      <span>6561234870</span>
    </div>
    <div class="contact contact-mail">
      <span class="contact-icon"><svg width="10" height="8" viewBox="0 0 10 8"><rect x=".5" y=".5" width="9" height="7" fill="none" stroke="#fff"/><path d="M.5 .5 5 4.5 9.5 .5" fill="none" stroke="#fff"/></svg></span>
      <span>care@corbinridgehealth.com</span>
    </div>
    <div class="contact contact-web">
      <span class="contact-icon"><svg width="10" height="10" viewBox="0 0 10 10"><circle cx="5" cy="5" r="4.3" fill="none" stroke="#fff"/><path d="M.7 5h8.6M5 .7c-2.2 2.4-2.2 6.2 0 8.6M5 .7c2.2 2.4 2.2 6.2 0 8.6" fill="none" stroke="#fff" stroke-width=".8"/></svg></span>
      <span>www.corbinridge.com</span>
    </div>
  </main>
</body>
</html>
```